Powerpoint template for Kestrel Pathway Advisors

I would like to use my logo and colors to create a powerpoint deck that I can use for various presentations. I would want the design to be modern, use my logo on each page (small at the bottom by the slide number) and have a couple of transition slides for cover page, transition page, etc.

```html
<!DOCTYPE html>
<html lang="en">
<head>
<meta charset="utf-8">
<title>Kestrel Pathway Advisors – Presentation Template</title>
<link rel="stylesheet" href="https://fonts.googleapis.com/css2?family=Poppins:wght@400;500;600;700&display=swap">
<style>
:root{
  --blue:#2f64e6;
  --blue-deep:#2455d6;
  --ink:#2a2a2d;
  --dark:#3d3e42;
  --grey:#8c8f96;
  --muted:#5a5c62;
  --rule:#d3d5da;
  --paper:#f4f5f8;
  --page:#f7f7f8;
  --white:#ffffff;
  --photo-a:#c9c6c0;
  --photo-b:#5b5a57;
}
*{box-sizing:border-box}
html,body{margin:0;width:707px;height:1200px;overflow:hidden;background:var(--page);font-family:'Poppins',sans-serif;color:var(--ink)}
.deck{display:grid;grid-template-columns:repeat(3,201px);gap:33px 17px;padding:33px 32px}
.slide{position:relative;width:201px;height:113px;background:var(--paper);overflow:hidden;box-shadow:0 1px 3px rgba(0,0,0,.14)}
.slide>*{position:absolute}
.slide.is-blue{background:var(--blue);color:var(--white)}
.meta{top:6px;right:14px;font-size:2px;color:#9a9ca3;white-space:nowrap}
.is-blue .meta{color:#dbe4ff}
.tick{top:11px;right:0;width:10px;height:.7px;background:var(--blue)}
.is-blue .tick{background:var(--white)}
.baseline{bottom:5px;left:0;right:30px;height:.3px;background:var(--rule)}
.brand{bottom:3px;right:6px;font-size:2.8px;font-weight:700;color:var(--blue);letter-spacing:.05em}
.is-blue .brand{color:var(--white)}
.kicker{font-size:1.8px;font-weight:700;letter-spacing:.35em;color:var(--blue);white-space:nowrap}
.is-blue .kicker{color:var(--white)}
.title{margin:0;font-size:9px;font-weight:600;line-height:.95;color:var(--ink)}
.is-blue .title{color:var(--white)}
.lorem{margin:0;font-size:2.1px;line-height:1.4;color:var(--muted);text-align:justify}
.is-blue .lorem{color:#e6ecff}
.caption{margin:0;font-size:2px;line-height:1.4;color:var(--muted);text-align:center}
.label{margin:0;font-size:2.1px;font-weight:700;color:var(--blue);text-align:center;white-space:nowrap}
.label.is-dark{color:var(--ink)}
.rule-short{width:10px;height:.5px;background:var(--blue)}
.photo{background:linear-gradient(135deg,var(--photo-a),var(--photo-b))}
.photo.is-light{background:linear-gradient(135deg,#eef0f3,#dcdfe4)}
.avatar{border-radius:50%;background:linear-gradient(160deg,#e3e5ea,#9fa3ab)}
.wordmark{font-weight:700;color:var(--blue);letter-spacing:.04em;line-height:1;text-align:center}
.wordmark small{display:block;font-weight:700;letter-spacing:.25em}
.cover-title{margin:0;font-weight:700;font-variant:small-caps;font-size:8px;line-height:1.1;color:var(--ink)}
.subtitle{margin:0;font-size:4px;color:var(--muted)}
.pill{display:flex;align-items:center;gap:4px;background:rgba(220,222,228,.8);border-radius:9px;padding:1.5px 14px 1.5px 1.5px}
.pill .avatar{width:14px;height:14px;border:1px solid var(--blue)}
.pill b{display:block;font-size:3.8px;color:var(--blue);font-weight:600}
.pill span{display:block;font-size:1.8px;color:var(--muted)}
.icon-dot{border-radius:50%;background:var(--blue);display:flex;align-items:center;justify-content:center}
.icon-dot.is-dark{background:var(--dark)}
.icon-dot svg{fill:var(--white)}
.overlay{left:0;top:0;width:201px;height:113px}
</style>
</head>
<body>
<svg width="0" height="0" style="position:absolute" aria-hidden="true">
  <symbol id="i-bank" viewBox="0 0 10 10"><path d="M5 1 9.5 3.4H.5Z M1.3 4h1.2v3.6H1.3Z M3.6 4h1.2v3.6H3.6Z M5.9 4h1.2v3.6H5.9Z M7.6 4h1.1v3.6H7.6Z M.6 8h8.8v1H.6Z"/></symbol>
  <symbol id="i-chart" viewBox="0 0 10 10"><path d="M1 1h.9v7.1H9V9H1Z M3 5h1.2v2.4H3Z M5 3.2h1.2v4.2H5Z M7 4.2h1.2v3.2H7Z"/></symbol>
  <symbol id="i-target" viewBox="0 0 10 10"><path d="M5 1a4 4 0 1 0 0 8 4 4 0 0 0 0-8Zm0 1.1a2.9 2.9 0 1 1 0 5.8 2.9 2.9 0 0 1 0-5.8Zm0 1.3a1.6 1.6 0 1 0 0 3.2 1.6 1.6 0 0 0 0-3.2Z"/></symbol>
  <symbol id="i-user" viewBox="0 0 10 10"><path d="M5 1a2.6 2.6 0 1 1 0 5.2A2.6 2.6 0 0 1 5 1Zm0 1.1a1.5 1.5 0 1 0 0 3 1.5 1.5 0 0 0 0-3ZM3 6.6l-.9 2.8h1.2L4 7.3Zm4 0 .9 2.8H6.7L6 7.3Z"/></symbol>
  <symbol id="i-home" viewBox="0 0 10 10"><path d="M5 1 9.5 5H8v4H6V6.4H4V9H2V5H.5Z"/></symbol>
  <symbol id="i-phone" viewBox="0 0 10 10"><path d="M2.4 1h5.2v8H2.4Zm1 1v5.4h3.2V2Zm1.1 6.1h1v.5h-1Z"/></symbol>
  <symbol id="i-people" viewBox="0 0 10 10"><circle cx="3" cy="3.3" r="1.4"/><circle cx="7" cy="3.3" r="1.4"/><path d="M.5 8.5c0-2 1-3 2.5-3s2.5 1 2.5 3Zm4 0c0-2 1-3 2.5-3s2.5 1 2.5 3Z"/></symbol>
  <symbol id="i-globe" viewBox="0 0 10 10"><path d="M5 1a4 4 0 1 0 0 8 4 4 0 0 0 0-8Zm0 1c.6.6 1 1.6 1.1 2.5H3.9C4 3.6 4.4 2.6 5 2Zm0 6c-.6-.6-1-1.6-1.1-2.5h2.2C6 6.4 5.6 7.4 5 8ZM2 4.5a3 3 0 0 1 1.6-2.2c-.4.7-.6 1.4-.7 2.2Zm0 1h.9c.1.8.3 1.5.7 2.2A3 3 0 0 1 2 5.5Zm6 0a3 3 0 0 1-1.6 2.2c.4-.7.6-1.4.7-2.2Zm0-1h-.9c-.1-.8-.3-1.5-.7-2.2A3 3 0 0 1 8 4.5Z"/></symbol>
  <symbol id="i-shuffle" viewBox="0 0 10 10"><path d="M1 2.5h2l4 5h1.5v-1l1.5 1.5L8.5 9.5v-1H6.5l-4-5H1Zm0 5h1.8l1-1.3.6.8-1.1 1.5H1Zm5.5-5h2v-1L10 3 8.5 4.5v-1H7l-1 1.3-.6-.8Z"/></symbol>
  <symbol id="i-link" viewBox="0 0 10 10"><path d="M4.2 3.4 5.6 2a2 2 0 0 1 2.8 2.8L7 6.2 6.3 5.5l1.4-1.4A1 1 0 0 0 6.3 2.7L4.9 4.1Zm1.6 3.2L4.4 8A2 2 0 0 1 1.6 5.2L3 3.8l.7.7-1.4 1.4a1 1 0 0 0 1.4 1.4l1.4-1.4ZM3.4 6 6 3.4l.6.6L4 6.6Z"/></symbol>
  <symbol id="i-send" viewBox="0 0 10 10"><path d="M9.5.5 .5 4.4l3.3 1.2L8 2 4.4 6.2 5.6 9.5Z"/></symbol>
  <symbol id="i-check" viewBox="0 0 10 10"><path d="M1.5 5.2 2.8 4l1.6 1.6L7.6 2.4 8.8 3.6 4.4 8Z"/></symbol>
</svg>

<main class="deck">

  <!-- 1 Cover, light with illustration -->
  <section class="slide">
    <div class="wordmark" style="left:13px;top:14px;font-size:6px;text-align:left">KESTREL<small style="font-size:1.3px">PATHWAY ADVISORS</small></div>
    <h1 class="cover-title" style="left:15px;top:43px">Presentation Title<br>Goes Here</h1>
    <p class="subtitle" style="left:15px;top:68px">Subtitle here</p>
    <div class="pill" style="left:14px;top:81px"><div class="avatar" role="img" aria-label="Presenter portrait"></div><div><b>NAME HERE</b><span>General Manager</span></div></div>
    <div role="img" aria-label="Rising mountain and growth arrow illustration" style="right:0;bottom:0;width:125px;height:75px;border-radius:60px 0 0 0;background:linear-gradient(135deg,#6d6e72 0%,#4a4b4f 40%,var(--blue) 75%)"></div>
  </section>

  <!-- 2 Cover, centred light -->
  <section class="slide">
    <div class="photo is-light" role="img" aria-label="Soft office background photograph" style="inset:0"></div>
    <div class="wordmark" style="left:0;right:0;top:28px;font-size:13px">KESTREL<small style="font-size:2.8px;color:var(--dark);margin-top:1px">PATHWAY ADVISORS</small></div>
    <h1 class="cover-title" style="left:0;right:0;top:55px;text-align:center">Presentation Title<br>Goes Here</h1>
    <p class="subtitle" style="left:0;right:0;top:78px;text-align:center">Subtitle here</p>
    <div class="pill" style="left:78px;top:88px"><div class="avatar" role="img" aria-label="Presenter portrait"></div><div><b>NAME HERE</b><span>General Manager</span></div></div>
  </section>

  <!-- 3 Cover, blue -->
  <section class="slide is-blue">
    <div class="wordmark" style="left:0;right:0;top:30px;font-size:13px;color:var(--white)">KESTREL<small style="font-size:2.8px;margin-top:1px">PATHWAY ADVISORS</small></div>
    <h1 class="cover-title" style="left:0;right:0;top:55px;text-align:center;color:var(--white)">Presentation Title<br>Goes Here</h1>
    <p class="subtitle" style="left:0;right:0;top:78px;text-align:center;color:var(--white)">Subtitle here</p>
  </section>

  <!-- 4 Agenda -->
  <section class="slide">
    <span class="meta">26 January 2026 &nbsp;|&nbsp; 4</span><i class="tick"></i><i class="baseline"></i><span class="brand">KESTREL</span>
    <h2 class="title" style="left:0;right:0;top:11px;text-align:center">Agenda Today</h2>
    <i class="rule-short" style="left:96px;top:24px"></i>
    <div style="left:22px;right:19px;top:30px;font-size:3px">
      <div style="display:flex;justify-content:space-between;border-bottom:.3px solid var(--rule);padding:1.6px 0;color:var(--blue)"><span>01. Welcome Message</span><b style="color:var(--ink)">Slide 02</b></div>
      <div style="display:flex;justify-content:space-between;border-bottom:.3px solid var(--rule);padding:1.6px 0;color:var(--muted)"><span>02. About Us</span><b style="color:var(--ink)">Slide 06</b></div>
      <div style="display:flex;justify-content:space-between;border-bottom:.3px solid var(--rule);padding:1.6px 0;color:var(--blue)"><span>03. What We Offer?</span><b style="color:var(--ink)">Slide 10</b></div>
      <div style="display:flex;justify-content:space-between;border-bottom:.3px solid var(--rule);padding:1.6px 0;color:var(--muted)"><span>04. How We Work?</span><b style="color:var(--ink)">Slide 17</b></div>
      <div style="display:flex;justify-content:space-between;border-bottom:.3px solid var(--rule);padding:1.6px 0;color:var(--blue)"><span>05. Team</span><b style="color:var(--ink)">Slide 20</b></div>
      <div style="display:flex;justify-content:space-between;border-bottom:.3px solid var(--rule);padding:1.6px 0;color:var(--muted)"><span>06. Contact Us</span><b style="color:var(--ink)">Slide 28</b></div>
    </div>
    <p style="left:46px;top:92px;margin:0;font-size:3.6px;font-weight:600;color:var(--blue);line-height:1.1;text-align:right">Lorem ipsum<br>dolor sit amet</p>
    <div style="left:79px;top:90px;width:93px;height:13px;background:var(--blue);border-radius:1px;display:flex;align-items:center;gap:4px;padding:0 4px">
      <span style="width:5px;height:5px;background:var(--dark);border-radius:1px;flex:none"></span>
      <span style="font-size:1.7px;color:var(--white);line-height:1.4">Lorem ipsum dolor sit amet, consectetuer adipiscing elit. Maecenas porttitor congue massa. Fusce posuere, magna sed pulvinar ultricies, purus.</span>
    </div>
  </section>

  <!-- 5 Title + text + mark -->
  <section class="slide">
    <span class="meta">26 January 2026 &nbsp;|&nbsp; 5</span><i class="tick"></i><i class="baseline"></i><span class="brand">KESTREL</span>
    <span class="kicker" style="left:11px;top:16px">DEMO SLIDE</span>
    <h2 class="title" style="left:11px;top:20px">Title Text<br>Demo</h2>
    <p class="lorem" style="left:11px;top:48px;width:93px">Lorem ipsum dolor sit amet, consectetuer adipiscing elit. Maecenas porttitor congue massa. Fusce posuere, magna sed pulvinar ultricies, purus lectus malesuada libero, sit amet commodo magna eros quis urna. Lorem ipsum dolor sit amet, consectetuer adipiscing elit. Maecenas porttitor congue massa. Fusce posuere, magna sed pulvinar ultricies, purus lectus malesuada libero, sit amet commodo magna eros quis urna. Lorem ipsum dolor sit amet, consectetuer adipiscing elit. Maecenas porttitor congue massa. Fusce posuere, magna sed pulvinar ultricies, purus lectus malesuada libero, sit amet commodo magna eros quis urna.</p>
    <div class="wordmark" style="left:118px;top:50px;font-size:12px">KESTREL</div>
  </section>

  <!-- 6 Diagonal blue + photo -->
  <section class="slide">
    <span class="meta">26 January 2026 &nbsp;|&nbsp; 6</span><i class="tick"></i><i class="baseline"></i><span class="brand">KESTREL</span>
    <div style="inset:0;background:var(--blue);clip-path:polygon(0 0,30% 0,43% 100%,0 100%)"></div>
    <div class="photo" role="img" aria-label="Empty office desk in window light" style="left:13px;top:27px;width:61px;height:57px"></div>
    <span class="kicker" style="left:92px;top:16px">DEMO SLIDE</span>
    <h2 class="title" style="left:92px;top:21px">Title Text Demo</h2>
    <p class="lorem" style="left:92px;top:42px;width:93px">Lorem ipsum dolor sit amet, consectetuer adipiscing elit. Maecenas porttitor congue massa. Fusce posuere, magna sed pulvinar ultricies, purus lectus malesuada libero, sit amet commodo magna eros quis urna. Lorem ipsum dolor sit amet, consectetuer adipiscing elit. Maecenas porttitor congue massa. Fusce posuere, magna sed pulvinar ultricies, purus lectus malesuada libero, sit amet commodo magna eros quis urna. Lorem ipsum dolor sit amet, consectetuer adipiscing elit. Maecenas porttitor congue massa. Fusce posuere, magna sed pulvinar ultricies, purus lectus malesuada libero.</p>
  </section>

  <!-- 7 Right-aligned title + block -->
  <section class="slide">
    <span class="meta">26 January 2026 &nbsp;|&nbsp; 7</span><i class="tick"></i><i class="baseline"></i><span class="brand">KESTREL</span>
    <span class="kicker" style="right:124px;top:16px">DEMO SLIDE</span>
    <h2 class="title" style="right:124px;top:20px;text-align:right">Title Text<br>Demo</h2>
    <p class="lorem" style="left:86px;top:22px;width:68px">Lorem Ipsum is simply dummy text of the printing and typesetting industry. Lorem Ipsum has been the industry's standard dummy text ever since the 1500s, when an unknown printer took a galley of type and scrambled it to make a type specimen book. It has survived not only five centuries, but also the leap into electronic typesetting, remaining essentially unchanged. It was popularised in the 1960s with the release of Letraset sheets containing Lorem Ipsum passages, and more recently with desktop publishing software.</p>
    <div style="left:85px;top:85px;width:70px;height:28px;background:var(--blue)"></div>
  </section>

  <!-- 8 Text + blue column + photo -->
  <section class="slide">
    <span class="meta">26 January 2026 &nbsp;|&nbsp; 8</span><i class="tick"></i><i class="baseline"></i><span class="brand">KESTREL</span>
    <p class="lorem" style="left:12px;top:22px;width:68px">Lorem Ipsum is simply dummy text of the printing and typesetting industry. Lorem Ipsum has been the industry's standard dummy text ever since the 1500s, when an unknown printer took a galley of type and scrambled it to make a type specimen book. It has survived not only five centuries, but also the leap into electronic typesetting, remaining essentially unchanged. It was popularised in the 1960s with the release of Letraset sheets containing Lorem Ipsum passages.</p>
    <div style="left:84px;top:0;width:70px;height:113px;background:var(--blue)"></div>
    <div class="photo" role="img" aria-label="Empty office desk in window light" style="left:117px;top:28px;width:70px;height:49px"></div>
  </section>

  <!-- 9 Three photos -->
  <section class="slide">
    <span class="meta">26 January 2026 &nbsp;|&nbsp; 9</span><i class="tick"></i><i class="baseline"></i><span class="brand">KESTREL</span>
    <span class="kicker" style="left:11px;top:16px">DEMO SLIDE</span>
    <h2 class="title" style="left:11px;top:21px">Title Text Demo</h2>
    <div class="photo" role="img" aria-label="Business person using a digital checklist" style="left:10px;top:40px;width:56px;height:32px;background:linear-gradient(135deg,#7d8fa8,#2d3a4f)"></div>
    <div class="photo" role="img" aria-label="Hands typing on a laptop" style="left:72px;top:40px;width:56px;height:32px;background:linear-gradient(135deg,#e4e6ea,#8e949c)"></div>
    <div class="photo" role="img" aria-label="Analyst reviewing charts" style="left:134px;top:40px;width:56px;height:32px;background:linear-gradient(135deg,#b7c2cc,#5e6b75)"></div>
    <p class="caption" style="left:10px;top:74px;width:56px">Lorem ipsum dolor sit amet, consectetuer adipiscing elit. Maecenas porttitor congue massa.</p>
    <p class="caption" style="left:72px;top:74px;width:56px">Lorem ipsum dolor sit amet, consectetuer adipiscing elit. Maecenas porttitor congue massa.</p>
    <p class="caption" style="left:134px;top:74px;width:56px">Lorem ipsum dolor sit amet, consectetuer adipiscing elit. Maecenas porttitor congue massa.</p>
  </section>

  <!-- 10 Blue centred text -->
  <section class="slide is-blue">
    <span class="meta">26 January 2026 &nbsp;|&nbsp; 10</span><i class="tick"></i><span class="brand">KESTREL</span>
    <span class="kicker" style="left:0;right:0;top:16px;text-align:center">DEMO SLIDE</span>
    <h2 class="title" style="left:0;right:0;top:21px;text-align:center">Title Text<br>Demo</h2>
    <p class="lorem" style="left:55px;top:47px;width:92px;text-align:center">Lorem ipsum dolor sit amet, consectetuer adipiscing elit. Maecenas porttitor congue massa. Fusce posuere, magna sed pulvinar ultricies, purus lectus malesuada libero, sit amet commodo magna eros quis urna. Lorem ipsum dolor sit amet, consectetuer adipiscing elit. Maecenas porttitor congue massa. Fusce posuere, magna sed pulvinar ultricies, purus lectus malesuada libero, sit amet commodo magna eros quis urna. Lorem ipsum dolor sit amet, consectetuer adipiscing elit. Maecenas porttitor congue massa.</p>
    <span style="left:83px;top:95px;width:34px;height:5px;border-radius:3px;background:var(--dark);font-size:2px;color:var(--white);display:flex;align-items:center;justify-content:center">Learn more</span>
  </section>

  <!-- 11 Steps + concentric rings -->
  <section class="slide">
    <span class="meta">26 January 2026 &nbsp;|&nbsp; 11</span><i class="tick"></i><i class="baseline"></i><span class="brand">KESTREL</span>
    <span class="kicker" style="left:11px;top:16px">DEMO SLIDE</span>
    <h2 class="title" style="left:11px;top:20px">Title Text<br>Demo</h2>
    <i class="rule-short" style="left:11px;top:42px"></i>
    <p class="lorem" style="left:11px;top:48px;width:76px">Lorem ipsum dolor sit amet, consectetuer adipiscing elit. Maecenas porttitor congue massa. Fusce posuere, magna sed pulvinar ultricies, purus lectus malesuada libero, sit amet commodo magna eros quis urna. Lorem ipsum dolor sit amet, consectetuer adipiscing elit. Fusce posuere, magna sed pulvinar ultricies, purus lectus malesuada libero, sit amet commodo magna eros quis urna.</p>
    <svg class="overlay" viewBox="0 0 201 113" aria-hidden="true" font-family="Poppins, sans-serif">
      <g font-size="4" font-weight="600" fill="#2a2a2d">
        <text x="95" y="17">+87%</text><text x="95" y="40">+68%</text><text x="95" y="63">+50%</text><text x="95" y="86">+43%</text>
      </g>
      <g fill="none" stroke="#2f64e6" stroke-width=".5">
        <rect x="95" y="24" width="16" height="3.4" rx="1.7"/><rect x="95" y="47" width="16" height="3.4" rx="1.7"/><rect x="95" y="70" width="16" height="3.4" rx="1.7"/><rect x="95" y="93" width="16" height="3.4" rx="1.7"/>
      </g>
      <g font-size="1.6" fill="#2f64e6" letter-spacing=".3"><text x="98" y="26.3">STEP #1</text><text x="98" y="49.3">STEP #2</text><text x="98" y="72.3">STEP #3</text><text x="98" y="95.3">STEP #4</text></g>
      <g stroke="#c8cacf" stroke-width=".3" stroke-dasharray="1 1" fill="none">
        <path d="M111 25.7 122 35"/><path d="M111 48.7 122 53"/><path d="M111 71.7 124 66"/><path d="M111 94.7 124 82"/>
      </g>
      <g fill="none" stroke="#e1e3e8">
        <circle cx="155" cy="57" r="33" stroke-width="4"/><circle cx="155" cy="57" r="26" stroke-width="3.5"/><circle cx="155" cy="57" r="19" stroke-width="3"/>
      </g>
      <g fill="none" transform="rotate(-90 155 57)">
        <circle cx="155" cy="57" r="33" stroke="#2f64e6" stroke-width="4" pathLength="100" stroke-dasharray="75 100"/>
        <circle cx="155" cy="57" r="26" stroke="#3d3e42" stroke-width="3.5" pathLength="100" stroke-dasharray="60 100"/>
        <circle cx="155" cy="57" r="19" stroke="#2f64e6" stroke-width="3" pathLength="100" stroke-dasharray="50 100"/>
        <circle cx="155" cy="57" r="12" stroke="#3d3e42" stroke-width="2.5" pathLength="100" stroke-dasharray="43 100"/>
      </g>
    </svg>
  </section>

  <!-- 12 Step ribbons -->
  <section class="slide">
    <span class="meta">26 January 2026 &nbsp;|&nbsp; 12</span><i class="tick"></i><i class="baseline"></i><span class="brand">KESTREL</span>
    <span class="kicker" style="left:0;right:0;top:16px;text-align:center">DEMO SLIDE</span>
    <h2 class="title" style="left:0;right:0;top:21px;text-align:center">Title Text Demo</h2>
    <svg class="overlay" viewBox="0 0 201 113" aria-hidden="true" font-family="Poppins, sans-serif">
      <g stroke-width="9" stroke-linecap="butt" fill="none">
        <path d="M48 70 72 46" stroke="#2f64e6"/>
        <path d="M72 46 86 64 108 42 120 56 146 30" stroke="#3d3e42" stroke-linejoin="bevel"/>
      </g>
      <path d="M140 22 152 18 150 34Z" fill="#3d3e42"/>
      <g font-size="2.4" font-weight="700" fill="#fff" letter-spacing=".3">
        <text x="57" y="61" transform="rotate(-45 57 61)">STEP 01</text>
        <text x="93" y="57" transform="rotate(-45 93 57)">STEP 02</text>
        <text x="127" y="47" transform="rotate(-45 127 47)">STEP 03</text>
      </g>
      <g stroke="#fff" stroke-width="1.2">
        <circle cx="48" cy="71" r="5" fill="#2f64e6"/><circle cx="86" cy="66" r="5" fill="#2f64e6"/><circle cx="120" cy="58" r="5" fill="#2f64e6"/>
      </g>
      <g fill="#fff"><use href="#i-shuffle" x="45.5" y="68.5" width="5" height="5"/><use href="#i-link" x="83.5" y="63.5" width="5" height="5"/><use href="#i-send" x="117.5" y="55.5" width="5" height="5"/></g>
    </svg>
    <p class="caption" style="left:22px;top:86px;width:44px">Lorem ipsum dolor sit amet, consectetuer adipiscing elit. Maecenas porttitor congue</p>
    <p class="caption" style="left:68px;top:86px;width:44px">Lorem ipsum dolor sit amet, consectetuer adipiscing elit. Maecenas porttitor congue</p>
    <p class="caption" style="left:110px;top:86px;width:44px">Lorem ipsum dolor sit amet, consectetuer adipiscing elit. Maecenas porttitor congue</p>
  </section>

  <!-- 13 Section break -->
  <section class="slide">
    <div class="photo is-light" role="img" aria-label="Faded bright office interior" style="inset:0"></div>
    <div class="wordmark" style="left:21px;top:27px;font-size:12px;text-align:left">KESTREL<small style="font-size:2.8px;color:var(--dark);margin-top:1px">PATHWAY ADVISORS</small></div>
    <div style="left:21px;top:57px;width:24px;height:22px;background:var(--blue);color:var(--white);font-size:8px;font-weight:700;display:flex;align-items:center;justify-content:center">01</div>
    <i style="left:21px;top:79px;width:.8px;height:34px;background:var(--blue)"></i>
    <h2 style="left:30px;top:78px;margin:0;font-size:13px;font-weight:700;color:var(--ink);letter-spacing:.02em">SECTION BREAKS</h2>
  </section>

  <!-- 14 Four icon services -->
  <section class="slide">
    <span class="meta">26 January 2026 &nbsp;|&nbsp; 14</span><i class="tick"></i><i class="baseline"></i><span class="brand">KESTREL</span>
    <span class="kicker" style="left:11px;top:15px">DEMO SLIDE</span>
    <h2 class="title" style="left:11px;top:20px">Title Text Demo</h2>
    <div class="icon-dot" style="left:24px;top:40px;width:22px;height:22px"><svg width="7" height="7"><use href="#i-bank"/></svg></div>
    <div class="icon-dot" style="left:68px;top:40px;width:22px;height:22px"><svg width="7" height="7"><use href="#i-chart"/></svg></div>
    <div class="icon-dot is-dark" style="left:112px;top:40px;width:22px;height:22px"><svg width="7" height="7"><use href="#i-target"/></svg></div>
    <div class="icon-dot" style="left:156px;top:40px;width:22px;height:22px"><svg width="7" height="7"><use href="#i-user"/></svg></div>
    <p class="label" style="left:13px;top:68px;width:44px">DEMO TEXT FOR ADVISORS</p>
    <p class="label" style="left:57px;top:68px;width:44px">DEMO TEXT FOR ADVISORS</p>
    <p class="label is-dark" style="left:101px;top:68px;width:44px">DEMO TEXT FOR ADVISORS</p>
    <p class="label" style="left:145px;top:68px;width:44px">DEMO TEXT FOR ADVISORS</p>
    <p class="caption" style="left:16px;top:72px;width:38px">Lorem ipsum dolor sit amet, consectetuer adipiscing elit. Maecenas porttitor congue massa.</p>
    <p class="caption" style="left:60px;top:72px;width:38px">Lorem ipsum dolor sit amet, consectetuer adipiscing elit. Maecenas porttitor congue massa.</p>
    <p class="caption" style="left:104px;top:72px;width:38px">Lorem ipsum dolor sit amet, consectetuer adipiscing elit. Maecenas porttitor congue massa.</p>
    <p class="caption" style="left:148px;top:72px;width:38px">Lorem ipsum dolor sit amet, consectetuer adipiscing elit. Maecenas porttitor congue massa.</p>
  </section>

  <!-- 15 Checklist -->
  <section class="slide">
    <div class="photo is-light" role="img" aria-label="Faded bright office interior" style="inset:0"></div>
    <span class="meta">26 January 2026 &nbsp;|&nbsp; 15</span><i class="tick"></i><i class="baseline"></i><span class="brand">KESTREL</span>
    <span class="kicker" style="left:11px;top:16px">DEMO SLIDE</span>
    <h2 class="title" style="left:11px;top:20px">Title Text<br>Demo</h2>
    <ul style="left:11px;top:48px;width:180px;margin:0;padding:0;list-style:none;font-size:2.2px;line-height:1.35;color:var(--muted)">
      <li style="display:flex;gap:1.5px"><svg width="2.4" height="2.4" style="flex:none;margin-top:.3px;fill:var(--blue)"><use href="#i-check"/></svg>Lorem ipsum dolor sit amet, consectetuer adipiscing elit. Maecenas porttitor congue massa.</li>
      <li style="display:flex;gap:1.5px"><svg width="2.4" height="2.4" style="flex:none;margin-top:.3px;fill:var(--blue)"><use href="#i-check"/></svg>Fusce posuere, magna sed pulvinar ultricies, purus lectus malesuada libero, sit amet commodo magna eros quis urna. Lorem ipsum dolor sit amet, consectetuer adipiscing elit. Maecenas porttitor congue massa.</li>
      <li style="display:flex;gap:1.5px"><svg width="2.4" height="2.4" style="flex:none;margin-top:.3px;fill:var(--blue)"><use href="#i-check"/></svg>Lorem ipsum dolor sit amet, consectetuer adipiscing elit. Maecenas porttitor congue massa.</li>
      <li style="display:flex;gap:1.5px"><svg width="2.4" height="2.4" style="flex:none;margin-top:.3px;fill:var(--blue)"><use href="#i-check"/></svg>Fusce posuere, magna sed pulvinar ultricies, purus lectus malesuada libero, sit amet commodo magna eros quis urna. Lorem ipsum dolor sit amet, consectetuer adipiscing elit. Maecenas porttitor congue massa.</li>
      <li style="display:flex;gap:1.5px"><svg width="2.4" height="2.4" style="flex:none;margin-top:.3px;fill:var(--blue)"><use href="#i-check"/></svg>Lorem ipsum dolor sit amet, consectetuer adipiscing elit. Maecenas porttitor congue massa. Lorem ipsum dolor sit amet, consectetuer adipiscing elit. Maecenas porttitor congue massa. Lorem ipsum dolor sit amet.</li>
      <li style="display:flex;gap:1.5px"><svg width="2.4" height="2.4" style="flex:none;margin-top:.3px;fill:var(--blue)"><use href="#i-check"/></svg>Lorem ipsum dolor sit amet, consectetuer adipiscing elit. Maecenas porttitor congue massa.</li>
      <li style="display:flex;gap:1.5px"><svg width="2.4" height="2.4" style="flex:none;margin-top:.3px;fill:var(--blue)"><use href="#i-check"/></svg>Fusce posuere, magna sed pulvinar ultricies, purus lectus malesuada libero, sit amet commodo magna eros quis urna. Lorem ipsum dolor sit amet, consectetuer adipiscing elit.</li>
      <li style="display:flex;gap:1.5px"><svg width="2.4" height="2.4" style="flex:none;margin-top:.3px;fill:var(--blue)"><use href="#i-check"/></svg>Lorem ipsum dolor sit amet, consectetuer adipiscing elit. Maecenas porttitor congue massa. Lorem ipsum dolor sit amet.</li>
    </ul>
  </section>

  <!-- 16 Blue numbered list -->
  <section class="slide is-blue">
    <span class="meta">26 January 2026 &nbsp;|&nbsp; 16</span><i class="tick"></i><span class="brand">KESTREL</span>
    <span class="kicker" style="left:11px;top:15px">DEMO SLIDE</span>
    <h2 class="title" style="left:11px;top:20px">Title Text Demo</h2>
    <i class="rule-short" style="left:11px;top:31px;background:var(--white)"></i>
    <div style="left:14px;top:42px;width:10px;height:10px;border-radius:50%;background:var(--white);color:var(--ink);font-size:3px;font-weight:700;display:flex;align-items:center;justify-content:center">01</div>
    <div style="left:101px;top:42px;width:10px;height:10px;border-radius:50%;background:var(--white);color:var(--ink);font-size:3px;font-weight:700;display:flex;align-items:center;justify-content:center">02</div>
    <div style="left:14px;top:75px;width:10px;height:10px;border-radius:50%;background:var(--white);color:var(--ink);font-size:3px;font-weight:700;display:flex;align-items:center;justify-content:center">03</div>
    <div style="left:101px;top:75px;width:10px;height:10px;border-radius:50%;background:var(--white);color:var(--ink);font-size:3px;font-weight:700;display:flex;align-items:center;justify-content:center">04</div>
    <div style="left:31px;top:43px;width:55px"><b style="font-size:2.3px;font-weight:600">DEMO TEXT FOR ADVISORS</b><p class="lorem" style="text-align:left;margin-top:1px">Lorem ipsum dolor sit amet, consectetuer adipiscing elit. Maecenas porttitor congue massa.</p></div>
    <div style="left:118px;top:43px;width:55px"><b style="font-size:2.3px;font-weight:600">DEMO TEXT FOR ADVISORS</b><p class="lorem" style="text-align:left;margin-top:1px">Lorem ipsum dolor sit amet, consectetuer adipiscing elit. Maecenas porttitor congue massa.</p></div>
    <div style="left:31px;top:76px;width:55px"><b style="font-size:2.3px;font-weight:600">DEMO TEXT FOR ADVISORS</b><p class="lorem" style="text-align:left;margin-top:1px">Lorem ipsum dolor sit amet, consectetuer adipiscing elit. Maecenas porttitor congue massa.</p></div>
    <div style="left:118px;top:76px;width:55px"><b style="font-size:2.3px;font-weight:600">DEMO TEXT FOR ADVISORS</b><p class="lorem" style="text-align:left;margin-top:1px">Lorem ipsum dolor sit amet, consectetuer adipiscing elit. Maecenas porttitor congue massa.</p></div>
  </section>

  <!-- 17 Progress donuts -->
  <section class="slide">
    <span class="meta">26 January 2026 &nbsp;|&nbsp; 17</span><i class="tick"></i><i class="baseline"></i><span class="brand">KESTREL</span>
    <span class="kicker" style="left:11px;top:15px">DEMO SLIDE</span>
    <h2 class="title" style="left:11px;top:20px">Title Text Demo</h2>
    <svg class="overlay" viewBox="0 0 201 113" aria-hidden="true" font-family="Poppins, sans-serif">
      <g fill="none" stroke="#dfe1e6" stroke-width="1.4">
        <circle cx="35" cy="48" r="11"/><circle cx="79" cy="48" r="11"/><circle cx="123" cy="48" r="11"/><circle cx="167" cy="48" r="11"/>
      </g>
      <g fill="#3d3e42"><circle cx="35" cy="48" r="8"/><circle cx="79" cy="48" r="8"/><circle cx="123" cy="48" r="8"/><circle cx="167" cy="48" r="8"/></g>
      <g fill="none" stroke="#2f64e6" stroke-width="1.8">
        <circle cx="35" cy="48" r="11" pathLength="100" stroke-dasharray="58 100" transform="rotate(-90 35 48)"/>
        <circle cx="79" cy="48" r="11" pathLength="100" stroke-dasharray="65 100" transform="rotate(-90 79 48)"/>
        <circle cx="123" cy="48" r="11" pathLength="100" stroke-dasharray="35 100" transform="rotate(-90 123 48)"/>
        <circle cx="167" cy="48" r="11" pathLength="100" stroke-dasharray="65 100" transform="rotate(-90 167 48)"/>
      </g>
      <g font-size="2.8" font-weight="600" fill="#2f64e6" text-anchor="middle">
        <text x="35" y="49">58%</text><text x="79" y="49">65%</text><text x="123" y="49">35%</text><text x="167" y="49">65%</text>
      </g>
    </svg>
    <p class="label" style="left:13px;top:67px;width:44px">DEMO TEXT FOR ADVISORS</p>
    <p class="label" style="left:57px;top:67px;width:44px">DEMO TEXT FOR ADVISORS</p>
    <p class="label" style="left:101px;top:67px;width:44px">DEMO TEXT FOR ADVISORS</p>
    <p class="label" style="left:145px;top:67px;width:44px">DEMO TEXT FOR ADVISORS</p>
    <p class="caption" style="left:16px;top:71px;width:38px">Lorem ipsum dolor sit amet, consectetuer adipiscing elit. Maecenas porttitor congue massa.</p>
    <p class="caption" style="left:60px;top:71px;width:38px">Lorem ipsum dolor sit amet, consectetuer adipiscing elit. Maecenas porttitor congue massa.</p>
    <p class="caption" style="left:104px;top:71px;width:38px">Lorem ipsum dolor sit amet, consectetuer adipiscing elit. Maecenas porttitor congue massa.</p>
    <p class="caption" style="left:148px;top:71px;width:38px">Lorem ipsum dolor sit amet, consectetuer adipiscing elit. Maecenas porttitor congue massa.</p>
  </section>

  <!-- 18 Text + bar chart -->
  <section class="slide">
    <span class="meta">26 January 2026 &nbsp;|&nbsp; 18</span><i class="tick"></i><i class="baseline"></i><span class="brand">KESTREL</span>
    <span class="kicker" style="left:11px;top:16px">DEMO SLIDE</span>
    <h2 class="title" style="left:11px;top:21px">Title Text Demo</h2>
    <p class="lorem" style="left:11px;top:42px;width:88px">Lorem ipsum dolor sit amet, consectetuer adipiscing elit. Maecenas porttitor congue massa. Fusce posuere, magna sed pulvinar ultricies, purus lectus malesuada libero, sit amet commodo magna eros quis urna. Lorem ipsum dolor sit amet, consectetuer adipiscing elit. Maecenas porttitor congue massa. Fusce posuere, magna sed pulvinar ultricies, purus lectus malesuada libero, sit amet commodo magna eros quis urna. Lorem ipsum dolor sit amet, consectetuer adipiscing elit. Maecenas porttitor congue massa. Fusce posuere, magna sed pulvinar ultricies.</p>
    <svg class="overlay" viewBox="0 0 201 113" aria-label="Bar chart of three series across four categories" role="img" font-family="Poppins, sans-serif">
      <text x="153" y="40" font-size="3.2" font-weight="600" fill="#2a2a2d" text-anchor="middle">Chart Title</text>
      <g font-size="1.8" fill="#8c8f96" text-anchor="end">
        <text x="115" y="85">0</text><text x="115" y="78.6">1</text><text x="115" y="72.2">2</text><text x="115" y="65.8">3</text><text x="115" y="59.4">4</text><text x="115" y="53">5</text><text x="115" y="46.6">6</text>
      </g>
      <path d="M118 84.4H192" stroke="#d3d5da" stroke-width=".3"/>
      <g fill="#2f64e6"><rect x="121" y="56.8" width="3.2" height="27.6"/><rect x="139" y="68.4" width="3.2" height="16"/><rect x="157" y="62" width="3.2" height="22.4"/><rect x="175" y="55.6" width="3.2" height="28.8"/></g>
      <g fill="#b4b7be"><rect x="125" y="69" width="3.2" height="15.4"/><rect x="143" y="56.2" width="3.2" height="28.2"/><rect x="161" y="72.8" width="3.2" height="11.6"/><rect x="179" y="66.6" width="3.2" height="17.8"/></g>
      <g fill="#3d3e42"><rect x="129" y="71.6" width="3.2" height="12.8"/><rect x="147" y="72.8" width="3.2" height="11.6"/><rect x="165" y="65.2" width="3.2" height="19.2"/><rect x="183" y="52.4" width="3.2" height="32"/></g>
      <g font-size="1.8" fill="#8c8f96" text-anchor="middle"><text x="126.6" y="88">Category 1</text><text x="144.6" y="88">Category 2</text><text x="162.6" y="88">Category 3</text><text x="180.6" y="88">Category 4</text></g>
      <g font-size="1.6" fill="#8c8f96"><rect x="133" y="91" width="1.4" height="1.4" fill="#2f64e6"/><text x="135" y="92.3">Series 1</text><rect x="145" y="91" width="1.4" height="1.4" fill="#b4b7be"/><text x="147" y="92.3">Series 2</text><rect x="157" y="91" width="1.4" height="1.4" fill="#3d3e42"/><text x="159" y="92.3">Series 3</text></g>
    </svg>
  </section>

  <!-- 19 Timeline arrow -->
  <section class="slide">
    <span class="meta">26 January 2026 &nbsp;|&nbsp; 19</span><i class="tick"></i><i class="baseline"></i><span class="brand">KESTREL</span>
    <span class="kicker" style="left:11px;top:15px">DEMO SLIDE</span>
    <h2 class="title" style="left:11px;top:20px">Title Text Demo</h2>
    <i class="rule-short" style="left:11px;top:31px"></i>
    <svg class="overlay" viewBox="0 0 201 113" aria-hidden="true">
      <g stroke="#b4b7be" stroke-width=".3" stroke-dasharray="1 1"><path d="M65 44V62"/><path d="M115 44V62"/><path d="M40 70V88"/><path d="M90 70V88"/><path d="M140 70V88"/></g>
      <path d="M13 66H78" stroke="#2f64e6" stroke-width="4" stroke-linecap="round"/>
      <path d="M78 66H166" stroke="#3d3e42" stroke-width="4"/>
      <path d="M160 59 168 66 160 73" stroke="#2a2a2d" stroke-width="4" fill="none" stroke-linecap="round" stroke-linejoin="round"/>
      <g fill="#fff" stroke="#2f64e6" stroke-width=".6"><circle cx="40" cy="66" r="2.3"/><circle cx="65" cy="66" r="2.3"/><circle cx="90" cy="66" r="2.3"/><circle cx="115" cy="66" r="2.3"/><circle cx="140" cy="66" r="2.3"/></g>
    </svg>
    <div style="left:45px;top:33px;width:40px"><p class="label is-dark" style="text-align:left">DEMO TEXT FOR ADVISORS</p><p class="lorem" style="text-align:left">Lorem ipsum dolor sit amet, consectetuer adipiscing elit. Maecenas porttitor congue massa.</p></div>
    <div style="left:95px;top:33px;width:40px"><p class="label" style="text-align:left">DEMO TEXT FOR ADVISORS</p><p class="lorem" style="text-align:left">Lorem ipsum dolor sit amet, consectetuer adipiscing elit. Maecenas porttitor congue massa.</p></div>
    <div style="left:20px;top:86px;width:40px"><p class="label" style="text-align:left">DEMO TEXT FOR ADVISORS</p><p class="lorem" style="text-align:left">Lorem ipsum dolor sit amet, consectetuer adipiscing elit. Maecenas porttitor congue massa.</p></div>
    <div style="left:70px;top:86px;width:40px"><p class="label is-dark" style="text-align:left">DEMO TEXT FOR ADVISORS</p><p class="lorem" style="text-align:left">Lorem ipsum dolor sit amet, consectetuer adipiscing elit. Maecenas porttitor congue massa.</p></div>
    <div style="left:120px;top:86px;width:40px"><p class="label is-dark" style="text-align:left">DEMO TEXT FOR ADVISORS</p><p class="lorem" style="text-align:left">Lorem ipsum dolor sit amet, consectetuer adipiscing elit. Maecenas porttitor congue massa.</p></div>
  </section>

  <!-- 20 Three outlined cards -->
  <section class="slide">
    <span class="meta">26 January 2026 &nbsp;|&nbsp; 20</span><i class="tick"></i><i class="baseline"></i><span class="brand">KESTREL</span>
    <span class="kicker" style="left:11px;top:15px">DEMO SLIDE</span>
    <h2 class="title" style="left:11px;top:20px">Title Text Demo</h2>
    <div style="left:18px;top:37px;width:50px;height:64px;border:.6px solid var(--blue)"></div>
    <div style="left:74px;top:37px;width:50px;height:64px;border:.6px solid var(--dark)"></div>
    <div style="left:130px;top:37px;width:50px;height:64px;border:.6px solid var(--blue)"></div>
    <svg style="left:39px;top:46px;fill:var(--blue)" width="8" height="8"><use href="#i-bank"/></svg>
    <svg style="left:95px;top:46px;fill:var(--dark)" width="8" height="8"><use href="#i-chart"/></svg>
    <svg style="left:151px;top:46px;fill:var(--blue)" width="8" height="8"><use href="#i-target"/></svg>
    <p class="label" style="left:18px;top:65px;width:50px;font-size:1.9px">DEMO TEXT FOR ADVISORS</p>
    <p class="label is-dark" style="left:74px;top:65px;width:50px;font-size:1.9px">DEMO TEXT FOR ADVISORS</p>
    <p class="label" style="left:130px;top:65px;width:50px;font-size:1.9px">DEMO TEXT FOR ADVISORS</p>
    <p class="caption" style="left:22px;top:69px;width:42px">Lorem ipsum dolor sit amet, consectetuer adipiscing elit. Maecenas porttitor congue massa.</p>
    <p class="caption" style="left:78px;top:69px;width:42px">Lorem ipsum dolor sit amet, consectetuer adipiscing elit. Maecenas porttitor congue massa.</p>
    <p class="caption" style="left:134px;top:69px;width:42px">Lorem ipsum dolor sit amet, consectetuer adipiscing elit. Maecenas porttitor congue massa.</p>
    <span style="left:36px;top:90px;width:14px;height:3.2px;border:.3px solid var(--blue);border-radius:2px;font-size:1.3px;color:var(--blue);display:flex;align-items:center;justify-content:center">LEARN MORE</span>
    <span style="left:92px;top:92px;width:14px;height:3.2px;border:.3px solid var(--dark);border-radius:2px;font-size:1.3px;color:var(--dark);display:flex;align-items:center;justify-content:center">LEARN MORE</span>
    <span style="left:148px;top:90px;width:14px;height:3.2px;border:.3px solid var(--blue);border-radius:2px;font-size:1.3px;color:var(--blue);display:flex;align-items:center;justify-content:center">LEARN MORE</span>
  </section>

  <!-- 21 Team -->
  <section class="slide">
    <span class="meta">26 January 2026 &nbsp;|&nbsp; 21</span><i class="tick"></i><i class="baseline"></i><span class="brand">KESTREL</span>
    <span class="kicker" style="left:12px;top:16px">DEMO SLIDE</span>
    <h2 class="title" style="left:12px;top:20px">Title Text<br>Demo</h2>
    <p class="lorem" style="left:12px;top:44px;width:46px;text-align:left">Lorem ipsum dolor sit amet, consectetuer adipiscing elit. Maecenas porttitor congue massa. Fusce posuere, magna sed pulvinar ultricies, purus lectus malesuada libero, sit amet commodo.</p>
    <div style="left:63px;top:24px;width:85px;height:30px;background:var(--blue);border-radius:1px;display:flex;align-items:center;gap:4px;padding-left:6px">
      <div class="avatar" role="img" aria-label="Team member portrait" style="width:22px;height:22px;flex:none"></div>
      <div style="color:var(--white);font-size:3.6px;font-weight:600;line-height:1.15">NAME HERE<br>General Manager</div>
    </div>
    <div style="left:151px;top:24px;width:39px;height:30px;background:var(--blue);border-radius:1px;text-align:center;padding-top:3px;color:var(--white)"><div class="avatar" role="img" aria-label="Team member portrait" style="width:15px;height:15px;margin:0 auto"></div><div style="font-size:1.4px;font-weight:600;margin-top:3px;line-height:1.3">NAME HERE<br>Manager</div></div>
    <div style="left:63px;top:58px;width:39px;height:33px;background:var(--blue);border-radius:1px;text-align:center;padding-top:4px;color:var(--white)"><div class="avatar" role="img" aria-label="Team member portrait" style="width:15px;height:15px;margin:0 auto"></div><div style="font-size:1.4px;font-weight:600;margin-top:4px;line-height:1.3">NAME HERE<br>Staff</div></div>
    <div style="left:106px;top:58px;width:39px;height:33px;background:var(--blue);border-radius:1px;text-align:center;padding-top:4px;color:var(--white)"><div class="avatar" role="img" aria-label="Team member portrait" style="width:15px;height:15px;margin:0 auto"></div><div style="font-size:1.4px;font-weight:600;margin-top:4px;line-height:1.3">NAME HERE<br>Staff</div></div>
    <div style="left:151px;top:58px;width:39px;height:33px;background:var(--blue);border-radius:1px;text-align:center;padding-top:4px;color:var(--white)"><div class="avatar" role="img" aria-label="Team member portrait" style="width:15px;height:15px;margin:0 auto"></div><div style="font-size:1.4px;font-weight:600;margin-top:4px;line-height:1.3">NAME HERE<br>Staff</div></div>
  </section>

  <!-- 22 Laptop mockup -->
  <section class="slide">
    <span class="meta">26 January 2026 &nbsp;|&nbsp; 22</span><i class="tick"></i><i class="baseline"></i><span class="brand">KESTREL</span>
    <div style="left:0;top:0;width:55px;height:113px;background:var(--blue)"></div>
    <div class="photo" role="img" aria-label="Laptop showing an office desk photograph" style="left:0;top:19px;width:112px;height:77px;border-radius:0 3px 3px 0;background:linear-gradient(135deg,#2d2e31 0 4%,#cfccc6 5%,#6a6964 90%,#2d2e31 91%)"></div>
    <span class="kicker" style="left:108px;top:16px">DEMO SLIDE</span>
    <h2 class="title" style="left:108px;top:20px">Title Text<br>Demo</h2>
    <p class="lorem" style="left:108px;top:42px;width:80px">Lorem ipsum dolor sit amet, consectetuer adipiscing elit. Maecenas porttitor congue massa. Fusce posuere, magna sed pulvinar ultricies, purus lectus malesuada libero, sit amet commodo magna eros quis urna. Lorem ipsum dolor sit amet, consectetuer adipiscing elit. Maecenas porttitor congue massa. Fusce posuere, magna sed pulvinar ultricies, purus lectus malesuada libero, sit amet commodo magna eros quis urna. Lorem ipsum dolor sit amet, consectetuer adipiscing elit.</p>
  </section>

  <!-- 23 Four icon list -->
  <section class="slide">
    <span class="meta">26 January 2026 &nbsp;|&nbsp; 24</span><i class="tick"></i><i class="baseline"></i><span class="brand">KESTREL</span>
    <span class="kicker" style="left:11px;top:15px">DEMO SLIDE</span>
    <h2 class="title" style="left:11px;top:20px">Title Text Demo</h2>
    <i class="rule-short" style="left:11px;top:31px"></i>
    <div class="icon-dot" style="left:13px;top:44px;width:12px;height:12px"><svg width="5" height="5"><use href="#i-bank"/></svg></div>
    <div class="icon-dot" style="left:100px;top:44px;width:12px;height:12px"><svg width="5" height="5"><use href="#i-target"/></svg></div>
    <div class="icon-dot" style="left:13px;top:77px;width:12px;height:12px"><svg width="5" height="5"><use href="#i-chart"/></svg></div>
    <div class="icon-dot" style="left:100px;top:77px;width:12px;height:12px"><svg width="5" height="5"><use href="#i-user"/></svg></div>
    <div style="left:31px;top:44px;width:60px"><p class="label" style="text-align:left;font-size:1.8px">DEMO TEXT FOR ADVISORS</p><p class="lorem" style="text-align:left;margin-top:2px">Lorem ipsum dolor sit amet, consectetuer adipiscing elit. Maecenas porttitor congue massa. Lorem ipsum dolor sit amet, consectetuer adipiscing elit. Maecenas porttitor congue massa.</p></div>
    <div style="left:118px;top:44px;width:60px"><p class="label" style="text-align:left;font-size:1.8px">DEMO TEXT FOR ADVISORS</p><p class="lorem" style="text-align:left;margin-top:2px">Lorem ipsum dolor sit amet, consectetuer adipiscing elit. Maecenas porttitor congue massa. Lorem ipsum dolor sit amet, consectetuer adipiscing elit. Maecenas porttitor congue massa.</p></div>
    <div style="left:31px;top:77px;width:60px"><p class="label" style="text-align:left;font-size:1.8px">DEMO TEXT FOR ADVISORS</p><p class="lorem" style="text-align:left;margin-top:2px">Lorem ipsum dolor sit amet, consectetuer adipiscing elit. Maecenas porttitor congue massa. Lorem ipsum dolor sit amet, consectetuer adipiscing elit. Maecenas porttitor.</p></div>
    <div style="left:118px;top:77px;width:60px"><p class="label" style="text-align:left;font-size:1.8px">DEMO TEXT FOR ADVISORS</p><p class="lorem" style="text-align:left;margin-top:2px">Lorem ipsum dolor sit amet, consectetuer adipiscing elit. Maecenas porttitor congue massa. Lorem ipsum dolor sit amet, consectetuer adipiscing elit. Maecenas porttitor.</p></div>
  </section>

  <!-- 24 Thank you -->
  <section class="slide" style="background:linear-gradient(180deg,var(--paper) 0 42%,var(--blue) 66%)">
    <div class="wordmark" style="left:0;right:0;top:17px;font-size:9px">KESTREL<small style="font-size:2px;color:var(--dark);margin-top:1px">PATHWAY ADVISORS</small></div>
    <h2 style="left:0;right:0;top:43px;margin:0;text-align:center;font-size:11px;font-weight:700;color:var(--blue);letter-spacing:.03em">THANK YOU</h2>
    <div style="left:14px;right:14px;top:71px;display:grid;grid-template-columns:repeat(4,1fr);color:var(--white);text-align:center">
      <div style="border-right:.3px solid rgba(255,255,255,.6);padding:0 2px"><svg width="5" height="5" style="fill:var(--white)"><use href="#i-home"/></svg><div style="font-size:2.6px;font-weight:600">ADDRESS</div><div style="font-size:1.6px;line-height:1.3">Lorem ipsum dolor sit amet, consectetuer adipiscing elit.</div></div>
      <div style="border-right:.3px solid rgba(255,255,255,.6);padding:0 2px"><svg width="5" height="5" style="fill:var(--white)"><use href="#i-phone"/></svg><div style="font-size:2.6px;font-weight:600">PHONE</div><div style="font-size:1.6px;line-height:1.3">123 456 789<br>123 456 789</div></div>
      <div style="border-right:.3px solid rgba(255,255,255,.6);padding:0 2px"><svg width="5" height="5" style="fill:var(--white)"><use href="#i-people"/></svg><div style="font-size:2.6px;font-weight:600">SOCIAL MEDIA</div><div style="display:flex;justify-content:center;gap:2px;margin-top:1px"><i style="width:2.4px;height:2.4px;background:var(--white);border-radius:.4px"></i><i style="width:2.4px;height:2.4px;background:var(--white);border-radius:.4px"></i></div><div style="display:flex;justify-content:center;gap:2px;margin-top:1px"><i style="width:2.4px;height:2.4px;background:var(--white);border-radius:.4px"></i><i style="width:2.4px;height:2.4px;background:var(--white);border-radius:.4px"></i></div></div>
      <div style="padding:0 2px"><svg width="5" height="5" style="fill:var(--white)"><use href="#i-globe"/></svg><div style="font-size:2.6px;font-weight:600">WEBSITE</div><div style="font-size:1.6px;line-height:1.3">www.yourwebsite.com</div></div>
    </div>
  </section>

</main>
</body>
</html>
```